Thornwick Estates Managment Ltd website

Need a website To inform people/clients of the services we provide. 5 pages total with a local feel. Bristol, UK. I have logo artwork already is like the look based on
incorporate the artwork attached for theme, feel and colours fonts info etc

To best describe the business have a brief look at www.fernbaylettings.co.uk which is a local firm offering the same services. This is for your ref only and not to be copied.

Target Market(s)

Property Investors/Landlords

Coding

Coded - Design and coding required

Number of Pages Required

5+ page

Colors
0392cd
f68d4d

Requirements
Must have
• local feel. Possibly using some local architecture or historic landmarks etc. This is fexible.
• most also be mobile device compatible
Nice to have
• the membership logos - files attached: KTB, GHW, DVT and safebondhold.co.uk

```html
<!DOCTYPE html>
<html lang="en">
<head>
<meta charset="utf-8">
<title>Thornwick Estates Managment Ltd</title>
<link href="https://fonts.googleapis.com/css2?family=Ubuntu:wght@400;500;700&family=Open+Sans:wght@400;600;700&display=swap" rel="stylesheet">
<style>
:root{
  --blue:#0392cd;
  --orange:#f68d4d;
  --navy:#1c3a50;
  --footer:#22313d;
  --footer-deep:#182430;
  --ink:#333b42;
  --grey:#7a8087;
  --line:#e3e3e3;
  --white:#ffffff;
}
*{box-sizing:border-box;margin:0;padding:0}
html,body{width:1200px;height:2528px;overflow:hidden;background:var(--white)}
body{font-family:"Open Sans",Arial,sans-serif;color:var(--ink);position:relative}
h1,h2,h3,h4{font-family:"Ubuntu",Arial,sans-serif;font-weight:500}

/* header */
.site-header{position:relative;height:540px}
.sidebar{position:absolute;left:0;top:0;width:240px;height:540px;background:var(--white);padding:40px 0 0 40px;z-index:2}
.brand{display:flex;align-items:center;gap:10px;margin-bottom:52px}
.brand-mark{width:38px;height:38px;background:var(--blue)}
.brand-name{font-family:"Ubuntu",sans-serif;font-weight:700;color:var(--navy);font-size:20px;line-height:1.05}
.main-nav{list-style:none}
.main-nav li{display:flex;align-items:center;gap:14px;height:38px;font-size:13px;font-weight:600;color:var(--ink)}
.main-nav li.active{color:var(--orange)}
.nav-icon{width:16px;height:16px;flex:none}
.hero{position:absolute;left:240px;top:0;width:960px;height:540px;background:linear-gradient(180deg,#2f86cf 0%,#5aa6dc 35%,#9cc3d8 52%,#b9a58c 62%,#6f7a82 78%,#3d5366 100%)}
.hero-title{position:absolute;left:80px;top:52px;color:var(--white);font-family:"Ubuntu",sans-serif;font-weight:400;font-size:34px;line-height:1.2;text-shadow:0 1px 3px rgba(0,0,0,.25)}
.hero-title .with{font-size:30px}
.hero-title strong{font-weight:500;font-size:42px;color:var(--navy);text-shadow:none}

/* intro */
.intro{height:480px;text-align:center;padding-top:94px}
.intro h1{font-size:38px;color:var(--ink)}
.intro .lead{width:720px;margin:36px auto 0;color:var(--orange);font-size:17px;line-height:1.6}
.intro .rule{width:180px;height:2px;background:var(--orange);margin:30px auto}
.intro .body{width:740px;margin:0 auto;color:var(--grey);font-size:12.5px;line-height:1.75}

/* what we do */
.what-we-do{position:relative;height:360px}
.what-we-do .photo{position:absolute;inset:0;background:linear-gradient(180deg,#9fb2c2 0%,#b7b6ad 40%,#8f877a 70%,#5e625f 100%)}
.what-we-do svg.panel{position:absolute;left:0;top:0}
.what-we-do .copy{position:absolute;left:80px;top:34px;width:430px;color:var(--white)}
.what-we-do h2{font-size:40px;margin-bottom:22px}
.what-we-do p{font-size:12.5px;line-height:1.7;margin-bottom:14px}

/* services */
.services{height:500px;padding-top:44px}
.services h2{text-align:center;font-size:38px;color:var(--ink);margin-bottom:38px}
.service-grid{display:flex;gap:40px;padding:0 80px}
.service-card{width:230px;text-align:center}
.service-photo{height:158px;border:6px solid var(--orange);margin-bottom:20px}
.service-card h3{font-size:20px;color:var(--ink);margin-bottom:10px}
.service-card p{font-size:11.5px;line-height:1.65;color:var(--grey)}

/* partners */
.partners{margin:0 80px;height:124px;border:1px solid var(--line);display:flex;align-items:center}
.partners-label{position:relative;width:230px;height:124px;flex:none}
.partners-label span{position:absolute;left:26px;top:34px;color:var(--white);font-family:"Ubuntu",sans-serif;font-size:24px;line-height:1.15}
.partner-badges{display:flex;align-items:center;justify-content:space-around;flex:1;padding:0 20px}
.badge{height:64px}

/* footer */
.site-footer{position:absolute;left:0;top:2080px;width:1200px;height:400px;background:var(--footer);color:#c9d1d8;display:flex;padding:40px 80px 0}
.footer-col{width:260px}
.footer-col h4{color:var(--white);font-size:16px;margin-bottom:22px}
.footer-col ul{list-style:none}
.footer-col li{font-size:12px;line-height:2.2;display:flex;align-items:center;gap:10px}
.bullet{width:5px;height:5px;background:var(--orange);flex:none}
.contact-icon{width:16px;height:16px;flex:none}
.footer-col p{font-size:12px;line-height:1.7;margin-bottom:14px}
.signup{display:flex;flex-direction:column;gap:10px;width:200px}
.signup .field{height:30px;background:var(--white);color:#999;font-size:12px;padding:6px 10px}
.signup .button{width:96px;height:30px;background:var(--orange);color:var(--white);font-size:12px;font-weight:700;text-align:center;line-height:30px}
.social-square{width:18px;height:18px;background:var(--blue);flex:none}
.copyright{position:absolute;left:0;top:2480px;width:1200px;height:48px;background:var(--footer-deep);color:#8fa0ad;font-size:12px;text-align:center;line-height:48px}
</style>
</head>
<body>

<header class="site-header">
  <div class="sidebar">
    <div class="brand">
      <div class="brand-mark"></div>
      <div class="brand-name">Thornwick<br>Estates</div>
    </div>
    <ul class="main-nav">
      <li class="active"><svg class="nav-icon" viewBox="0 0 16 16"><path d="M2 8 8 2l6 6v6H10v-4H6v4H2z" fill="#f68d4d"/></svg>Home</li>
      <li><svg class="nav-icon" viewBox="0 0 16 16"><circle cx="8" cy="5" r="3" fill="#1c3a50"/><path d="M2 15c0-4 3-6 6-6s6 2 6 6z" fill="#1c3a50"/></svg>About Us</li>
      <li><svg class="nav-icon" viewBox="0 0 16 16"><rect x="2" y="3" width="12" height="11" fill="#1c3a50"/><rect x="5" y="6" width="2" height="2" fill="#fff"/><rect x="9" y="6" width="2" height="2" fill="#fff"/></svg>Landlords</li>
      <li><svg class="nav-icon" viewBox="0 0 16 16"><circle cx="5" cy="5" r="2.5" fill="#1c3a50"/><circle cx="11" cy="5" r="2.5" fill="#1c3a50"/><path d="M0 14c0-3 2-5 5-5s5 2 5 5zM6 14c0-3 2-5 5-5s5 2 5 5z" fill="#1c3a50"/></svg>Tenants</li>
      <li><svg class="nav-icon" viewBox="0 0 16 16"><circle cx="8" cy="8" r="6" fill="none" stroke="#1c3a50" stroke-width="3"/></svg>Services</li>
      <li><svg class="nav-icon" viewBox="0 0 16 16"><path d="M2 14l2-5 8-8 3 3-8 8z" fill="#1c3a50"/></svg>Blog</li>
      <li><svg class="nav-icon" viewBox="0 0 16 16"><rect x="1" y="3" width="14" height="10" fill="#1c3a50"/><path d="M1 3l7 6 7-6" fill="none" stroke="#fff" stroke-width="1.4"/></svg>Contact Us</li>
    </ul>
  </div>
  <div class="hero" role="img" aria-label="Photograph of colourful Bristol harbourside houses reflected in the water under a blue sky">
    <h2 class="hero-title">Going Above and Beyond To Find Your Next Home<br><span class="with">With </span><strong>Thornwick Estates Management</strong></h2>
  </div>
</header>

<section class="intro">
  <h1>We Are Thornwick Estates Managment Ltd</h1>
  <p class="lead">We manage homes across Bristol with care, giving landlords steady income and tenants well kept places to live, backed by local knowledge and honest advice.</p>
  <div class="rule"></div>
  <p class="body">From Clifton terraces to Harbourside flats, our team looks after every detail of your property. We find reliable tenants, arrange repairs, collect rent and keep you informed at every step, so your investment stays safe and your time stays free. Speak to us today about a plan that suits your portfolio.</p>
</section>

<section class="what-we-do">
  <div class="photo" role="img" aria-label="Photograph of a historic Bristol stone building with a busy street in front"></div>
  <svg class="panel" width="1200" height="360" viewBox="0 0 1200 360">
    <polygon points="0,0 640,0 480,360 0,360" fill="#f68d4d"/>
    <polygon points="640,0 668,0 508,360 480,360" fill="#ffffff"/>
  </svg>
  <div class="copy">
    <h2>What We Do</h2>
    <p>We handle the full letting journey for landlords, from valuing your property and marketing it to vetting tenants and drawing up tenancy agreements. Our local team knows the streets, the prices and the people, so every let starts on firm ground.</p>
    <p>Once tenants move in we keep things running, with rent collection, regular inspections and quick repairs through trusted local trades.</p>
  </div>
</section>

<section class="services">
  <h2>Our Management Services</h2>
  <div class="service-grid">
    <article class="service-card">
      <div class="service-photo" role="img" aria-label="Photograph of a modern Bristol office building" style="background:linear-gradient(180deg,#8fb3d3,#7c8a96)"></div>
      <h3>Finance</h3>
      <p>Clear monthly statements, prompt rent transfers and sound advice on yields help you plan ahead and grow your property income with confidence.</p>
    </article>
    <article class="service-card">
      <div class="service-photo" role="img" aria-label="Photograph of a row of period terraced houses" style="background:linear-gradient(180deg,#c9a98a,#8a6b55)"></div>
      <h3>Maintenance</h3>
      <p>Our trusted trades fix leaks, faults and wear quickly, and planned checks keep your property safe, legal and in good order.</p>
    </article>
    <article class="service-card">
      <div class="service-photo" role="img" aria-label="Photograph of a new residential development" style="background:linear-gradient(180deg,#b7c4cf,#8c7d6b)"></div>
      <h3>Property Developers</h3>
      <p>We help developers let new homes fast, with launch marketing, tenant matching and ongoing management for every unit in the scheme.</p>
    </article>
    <article class="service-card">
      <div class="service-photo" role="img" aria-label="Photograph of city apartment blocks" style="background:linear-gradient(180deg,#9ec3e0,#6d7f8e)"></div>
      <h3>Insurance</h3>
      <p>We arrange landlord cover and rent guarantee policies so your building, contents and income are protected against the unexpected.</p>
    </article>
  </div>
</section>

<section class="partners">
  <div class="partners-label">
    <svg width="230" height="124" viewBox="0 0 230 124"><polygon points="0,0 200,0 228,62 200,124 0,124" fill="#1c3a50"/></svg>
    <span>Our<br>Partners</span>
  </div>
  <div class="partner-badges">
    <svg class="badge" width="64" height="64" role="img" aria-label="KTB membership badge"><rect width="64" height="64" fill="#0392cd"/></svg>
    <svg class="badge" width="120" height="64" role="img" aria-label="DVT membership badge"><rect y="10" width="120" height="44" fill="#b08fc4"/></svg>
    <svg class="badge" width="80" height="64" role="img" aria-label="GHW membership badge"><rect x="8" width="64" height="64" fill="#8b2a2a"/></svg>
    <svg class="badge" width="170" height="64" role="img" aria-label="safebondhold.co.uk membership badge"><rect y="14" width="170" height="36" fill="#4a7bb6"/></svg>
  </div>
</section>

<footer class="site-footer">
  <div class="footer-col" style="width:230px">
    <h4>Quick Links</h4>
    <ul>
      <li><span class="bullet"></span>Home</li>
      <li><span class="bullet"></span>About Us</li>
      <li><span class="bullet"></span>Landlords</li>
      <li><span class="bullet"></span>Tenants</li>
      <li><span class="bullet"></span>Services</li>
      <li><span class="bullet"></span>Blog</li>
      <li><span class="bullet"></span>Contact Us</li>
    </ul>
  </div>
  <div class="footer-col" style="width:290px">
    <h4>Contact Information</h4>
    <ul>
      <li><svg class="contact-icon" viewBox="0 0 16 16"><path d="M8 1a5 5 0 0 1 5 5c0 4-5 9-5 9S3 10 3 6a5 5 0 0 1 5-5z" fill="#f68d4d"/><circle cx="8" cy="6" r="2" fill="#22313d"/></svg>Unit 4 Harbourside Quay, Bristol BS1 5TX</li>
      <li><svg class="contact-icon" viewBox="0 0 16 16"><path d="M3 1h3l1 4-2 1c1 2 3 4 5 5l1-2 4 1v3c0 1-1 2-2 2C7 15 1 9 1 3c0-1 1-2 2-2z" fill="#f68d4d"/></svg>+44 (0)117 496 0321</li>
      <li><svg class="contact-icon" viewBox="0 0 16 16"><rect x="1" y="3" width="14" height="10" fill="#f68d4d"/><path d="M1 3l7 6 7-6" fill="none" stroke="#22313d" stroke-width="1.4"/></svg>info@thornwickestates.co.uk</li>
    </ul>
  </div>
  <div class="footer-col" style="width:280px">
    <h4>Newsletter Signup</h4>
    <p>Sign up for local market news, tips and offers from our team.</p>
    <div class="signup">
      <div class="field">Your Email</div>
      <div class="button">Subscribe</div>
    </div>
  </div>
  <div class="footer-col" style="width:200px">
    <h4>Follow Us</h4>
    <ul>
      <li><span class="social-square"></span>Fanpage</li>
      <li><span class="social-square"></span>Linkwork</li>
      <li><span class="social-square"></span>Chirper</li>
      <li><span class="social-square"></span>Email</li>
    </ul>
  </div>
</footer>
<div class="copyright">© 2024 Thornwick Estates Managment Ltd</div>

</body>
</html>
```